Board Presentation template

Design a simple and clean PowerPoint slide templates for a Board meeting. The slides should have predominantly white backgrounds and use the colors of our Logo (attached): Tones of grey and orange and blue.
The company name is called Harbor Lane Gauges.
It sell, calibrate, service and repair industrial and commercial scales of all types. In particular, Truck scales, floor scales, counting scales and benchtop scales.
There is no website for Harbor Lane Gauges, but we have three affiliates that have their own websites:
https://www.tallyloadworks.com/
https://northbendbalanceandmeasure.com/
https://kvbalance.com/
Target Market(s)
Industrial and Commercial Weighing systems
Industry/Entity Type
Look and feel
Each slider illustrates characteristics of the customer's brand and the style your logo design should communicate.

```html
<!DOCTYPE html>
<html lang="en">
<head>
<meta charset="utf-8">
<title>Harbor Lane Gauges – Board Presentation Templates</title>
<link href="https://fonts.googleapis.com/css2?family=Poppins:wght@400;500;600;700&display=swap" rel="stylesheet">
<style>
  :root{
    --canvas:#a3a3a3;
    --white:#ffffff;
    --red:#cf3a2c;
    --blue:#2b5f8e;
    --blue-deep:#1f4d78;
    --ink:#1f2328;
    --charcoal:#2a2e33;
    --grey:#6b6f75;
    --grey-light:#d9d9d9;
    --grey-soft:#eeeeee;
  }
  *{margin:0;padding:0;box-sizing:border-box}
  html,body{width:1200px;height:675px;overflow:hidden;background:var(--canvas)}
  body{font-family:"Poppins",sans-serif;color:var(--ink)}
  .deck{position:relative;width:1200px;height:675px}
  .slide{position:absolute;width:268px;height:150px;background:var(--white);overflow:hidden}
  .c1{left:41px}.c2{left:324px}.c3{left:607px}.c4{left:891px}
  .r1{top:13px}.r2{top:179px}.r3{top:345px}.r4{top:512px}
  .abs{position:absolute}
  .rule{position:absolute;width:14px;height:4px;border-top:1px solid var(--red);border-left:1px solid var(--red)}
  .title{position:absolute;font-weight:700;font-size:8px;line-height:1.2;color:var(--ink)}
  .title .hl{color:var(--red)}
  .body{position:absolute;font-size:3.2px;line-height:1.55;color:var(--grey)}
  .body p{margin-bottom:2.5px}
  .body b{color:var(--ink);font-weight:600}
  .photo{position:absolute;background:linear-gradient(135deg,#8d96a0,#4b545d)}
  .badge{position:absolute;right:6px;bottom:-4px;width:22px;height:22px;border-radius:50%;border:1px solid var(--blue);background:var(--white);display:flex;align-items:center;justify-content:center;text-align:center}
  .badge span{font-size:2.2px;font-weight:600;color:var(--blue);line-height:1.1;width:16px;margin-top:-5px}
  .brand{position:absolute;text-align:center;display:flex;flex-direction:column;align-items:center}
  .brand .dot{width:7px;height:7px;border-radius:50%;background:var(--red);margin-bottom:1.5px}
  .brand .name{font-size:3px;font-weight:700;color:var(--charcoal);letter-spacing:.2px}
  /* title slides */
  .hero-title{position:absolute;font-weight:700;font-size:9px;line-height:1.2;color:var(--red)}
  .hero-sub{position:absolute;font-size:3.6px;font-weight:500}
  .hero-meta{position:absolute;font-size:3.2px}
  /* agenda */
  .agenda{position:absolute;left:120px;top:40px;width:140px;border-collapse:collapse;font-size:2.8px;color:var(--grey)}
  .agenda th{color:var(--red);font-weight:600;text-align:left;padding-bottom:3px;font-size:3.2px}
  .agenda td{padding:3px 0;border-top:.4px solid var(--grey-light);vertical-align:top}
  /* services */
  .service{position:absolute;top:60px;width:50px;text-align:center;font-size:3.6px;color:var(--grey);line-height:1.3}
  .service .ic{width:20px;height:20px;border-radius:50%;margin:0 auto 5px;display:flex;align-items:center;justify-content:center}
  /* team */
  .member{position:absolute;top:44px;width:42px;text-align:center}
  .member .ph{width:28px;height:28px;border-radius:50%;background:var(--grey-soft);margin:0 auto 3px;font-size:3.2px;color:#9a9a9a;display:flex;align-items:center;justify-content:center}
  .member .bar{height:8px;color:var(--white);font-size:2.8px;font-weight:600;line-height:1.1;padding-top:1px}
  .member .bar small{display:block;font-size:2px;font-weight:400}
  .member .txt{font-size:2.4px;color:var(--grey);line-height:1.5;margin-top:3px;text-align:left}
  .dark{background:var(--charcoal)}.blue{background:var(--blue)}
  /* profile */
  .item{position:absolute;left:138px;width:120px;display:flex;gap:5px}
  .item .ic{flex:none;width:7px;height:7px;border-radius:50%;background:var(--grey-soft)}
  .item h4{font-size:3.2px;color:var(--red);font-weight:600;margin-bottom:2px}
  .item p{font-size:2.6px;color:var(--grey);line-height:1.5}
  /* vision */
  .vcirc{position:absolute;width:30px;height:30px;border-radius:50%;border:3px solid var(--grey-soft);background-clip:padding-box}
  .vlabel{position:absolute;font-size:3px;font-weight:600;color:var(--ink)}
  .vtext{position:absolute;font-size:2.5px;line-height:1.5;color:var(--grey);width:50px}
  /* chart */
  .findings{position:absolute;left:188px;top:52px;width:72px}
  .findings .tag{background:var(--red);color:var(--white);font-size:3px;font-weight:600;padding:1.5px 3px}
  .findings p{font-size:2.6px;color:var(--grey);line-height:1.5;margin-top:3px}
  /* thank you */
  .thanks{background:linear-gradient(120deg,var(--blue-deep),#3d74a3 60%,#c9d6e2)}
  .contact{position:absolute;left:16px;top:100px;font-size:2.8px;color:var(--white)}
  .contact li{list-style:none;display:flex;align-items:center;gap:3px;margin-bottom:2px}
  .contact i{width:4px;height:4px;border-radius:50%;background:var(--white);display:inline-block}
</style>
</head>
<body>
<main class="deck">

  <!-- 1 Title light -->
  <section class="slide c1 r1" style="background:radial-gradient(circle at 50% 45%,#fff,#ececec)">
    <div class="brand" style="left:114px;top:7px;width:40px"><div class="dot"></div><div class="name">HARBOR LANE GAUGES</div></div>
    <div class="abs" style="left:127px;top:32px;width:14px;height:1px;background:var(--red)"></div>
    <div class="hero-title" style="left:0;top:47px;width:268px;text-align:center;font-size:10px">Presentation title here in this style</div>
    <div class="hero-sub" style="left:0;top:62px;width:268px;text-align:center;color:#9aa3ad">Subtitle of the presentation</div>
    <div class="hero-meta" style="left:0;top:82px;width:268px;text-align:center;color:var(--grey)">Speaker details here</div>
    <div class="hero-meta" style="left:0;top:98px;width:268px;text-align:center;color:var(--grey);font-size:2.6px">Date, Year</div>
    <div class="photo" role="img" aria-label="Row of weighing scales with a yellow truck on a scale" style="left:66px;top:110px;width:136px;height:40px;background:linear-gradient(90deg,#c9c9c9,#e4b43c 45%,#d0402f 60%,#b8c3cf)"></div>
  </section>

  <!-- 2 Title blue -->
  <section class="slide c2 r1">
    <div class="abs" style="left:120px;top:-40px;width:220px;height:220px;border-radius:50%;background:var(--blue)"></div>
    <div class="photo" role="img" aria-label="Yellow truck driving onto a weighbridge" style="left:140px;top:30px;width:110px;height:120px;background:linear-gradient(180deg,#e2a826 0%,#c99120 45%,#b9bfc6 75%,#8d949b)"></div>
    <div class="brand" style="left:12px;top:12px;width:28px"><div class="dot"></div><div class="name">HARBOR LANE GAUGES</div></div>
    <div class="abs" style="left:16px;top:34px;width:14px;height:1px;background:var(--red)"></div>
    <div class="hero-title" style="left:16px;top:43px;width:110px">Presentation title<br>here in this style</div>
    <div class="hero-sub" style="left:16px;top:68px;color:var(--ink)">Subtitle of the presentation</div>
    <div class="hero-meta" style="left:16px;top:86px;color:var(--grey)">Speaker details here</div>
    <div class="hero-meta" style="left:16px;top:135px;color:var(--grey);font-size:2.6px">Date, Year</div>
  </section>

  <!-- 3 Title dark -->
  <section class="slide c3 r1" style="background:var(--charcoal)">
    <div class="abs" style="left:135px;top:-30px;width:200px;height:210px;border-radius:50%;background:var(--red)"></div>
    <div class="photo" role="img" aria-label="Yellow truck driving onto a weighbridge" style="left:140px;top:30px;width:110px;height:120px;background:linear-gradient(180deg,#e2a826 0%,#c99120 45%,#b9bfc6 75%,#8d949b)"></div>
    <div class="brand" style="left:16px;top:0;width:30px;background:var(--white);padding:8px 2px 3px"><div class="dot"></div><div class="name">HARBOR LANE GAUGES</div></div>
    <div class="abs" style="left:16px;top:34px;width:14px;height:1px;background:var(--red)"></div>
    <div class="hero-title" style="left:16px;top:43px;width:110px;color:var(--white)">Presentation title<br>here in this style</div>
    <div class="hero-sub" style="left:16px;top:68px;color:var(--white)">Subtitle of the presentation</div>
    <div class="hero-meta" style="left:16px;top:86px;color:#c7c9cc">Speaker details here</div>
    <div class="hero-meta" style="left:16px;top:135px;color:#c7c9cc;font-size:2.6px">Date, Year</div>
  </section>

  <!-- 4 Agenda -->
  <section class="slide c4 r1">
    <div class="abs" style="left:-90px;top:-40px;width:190px;height:210px;border-radius:50%;background:var(--blue)"></div>
    <div class="photo" role="img" aria-label="Shopping basket of fresh produce on a retail scale" style="left:14px;top:45px;width:78px;height:100px;border-radius:4px;background:linear-gradient(180deg,#6aa83c,#d4452f 45%,#9aa5ae)"></div>
    <div class="title" style="left:122px;top:22px;font-size:8px"><span class="hl">A</span>genda</div>
    <table class="agenda">
      <tr><th>Time</th><th>Topic</th><th>Participants</th></tr>
      <tr><td>9:00 AM</td><td>Introduction &amp; Market Overview</td><td>CEO</td></tr>
      <tr><td>9:20 AM</td><td>Financial Performance Review</td><td>CFO</td></tr>
      <tr><td>9:50 AM</td><td>Core Business Review: Sales &amp; Calibration</td><td>VP of Sales</td></tr>
      <tr><td>10:30 AM</td><td style="color:var(--red)">— Break —</td><td></td></tr>
      <tr><td>10:45 AM</td><td>Service &amp; Reliability Operations</td><td>COO</td></tr>
      <tr><td>11:20 AM</td><td>Future Strategy &amp; Growth Initiatives</td><td>CEO / Strategy Lead</td></tr>
    </table>
    <div class="badge"><span>Harbor Lane Gauges</span></div>
  </section>

  <!-- 5 Introduction -->
  <section class="slide c1 r2">
    <div class="rule" style="left:16px;top:12px"></div>
    <div class="title" style="left:16px;top:24px">Introduction</div>
    <div class="body" style="left:16px;top:50px;width:122px">
      <p style="font-size:4.4px;font-weight:700;color:var(--blue)">Welcome.</p>
      <p><b style="color:var(--red)">Harbor Lane Gauges</b> is dedicated to keeping the weighing systems of our commercial and industrial clients accurate and compliant. We deliver <b>sales, calibration, preventative service and reliable repair</b> for all scale types.</p>
      <p>We understand that accuracy is critical to your bottom line, which is why we specialise in the most crucial systems, including <b>truck scales, floor scales, counting scales and benchtop scales</b>. Partner with us to protect your equipment and keep every weight you record precise and dependable.</p>
    </div>
    <div class="photo" role="img" aria-label="Truck wheel on an illuminated weighbridge at dusk" style="left:158px;top:22px;width:110px;height:128px;border-radius:10px 0 0 0;background:linear-gradient(160deg,#5e6a72,#2c3338 60%,#d9912c)"></div>
    <div class="badge"><span>Harbor Lane Gauges</span></div>
  </section>

  <!-- 6 Core Services -->
  <section class="slide c2 r2">
    <div class="rule" style="left:16px;top:12px"></div>
    <div class="title" style="left:16px;top:24px">Our Core Services</div>
    <div class="service" style="left:20px"><div class="ic" style="background:#3d4247"><svg width="10" height="10" viewBox="0 0 10 10"><rect x="1" y="6" width="8" height="2" fill="#fff"/><rect x="4" y="2" width="2" height="4" fill="#fff"/></svg></div>Sales:<br>High-Performance<br>Weighing Systems</div>
    <div class="service" style="left:80px"><div class="ic" style="background:var(--blue)"><svg width="10" height="10" viewBox="0 0 10 10"><rect x="2" y="1" width="6" height="8" fill="none" stroke="#fff"/><path d="M3.5 5l1.2 1.2L7 4" stroke="#fff" fill="none"/></svg></div>Calibration &amp;<br>Certification</div>
    <div class="service" style="left:140px"><div class="ic" style="background:var(--red)"><svg width="10" height="10" viewBox="0 0 10 10"><circle cx="5" cy="5" r="3" fill="none" stroke="#fff" stroke-width="1.2"/><circle cx="5" cy="5" r="1" fill="#fff"/></svg></div>Preventative<br>Service &amp;<br>Maintenance</div>
    <div class="service" style="left:200px"><div class="ic" style="background:var(--ink)"><svg width="10" height="10" viewBox="0 0 10 10"><path d="M2 8l4-4M6 2.5a1.8 1.8 0 1 0 1.5 1.5" stroke="#fff" stroke-width="1.2" fill="none"/></svg></div>Repair &amp;<br>Emergency<br>Service</div>
    <div class="badge"><span>Harbor Lane Gauges</span></div>
  </section>

  <!-- 7 Sales -->
  <section class="slide c3 r2">
    <div class="rule" style="left:16px;top:12px"></div>
    <div class="title" style="left:16px;top:22px"><span class="hl">Sales:</span> High-Performance<br>Weighing Systems</div>
    <div class="photo" role="img" aria-label="Red truck parked on a blue truck scale" style="left:16px;top:55px;width:122px;height:78px;border-radius:8px;background:linear-gradient(180deg,#c7d7e5 0%,#c7d7e5 40%,#b23a2c 55%,#3c6d9c 75%,#9a8f7a)"></div>
    <div class="body" style="left:180px;top:55px;width:78px">
      <p><b>Harbor Lane Gauges</b> partners with industry-leading manufacturers to provide a complete range of commercial and industrial scales tailored to your operation. We offer a consultation to match your needs, whether it is high-capacity <b>Truck Scales</b>, rugged <b>Floor Scales</b>, or precise <b>Counting and Benchtop Scales</b>, with the ideal equipment. Our goal is to supply reliable systems that drive efficiency from day one.</p>
    </div>
    <div class="badge"><span>Harbor Lane Gauges</span></div>
  </section>

  <!-- 8 Calibration -->
  <section class="slide c4 r2">
    <div class="rule" style="left:16px;top:12px"></div>
    <div class="title" style="left:16px;top:24px">Calibration &amp;<br>Certification</div>
    <div class="body" style="left:16px;top:58px;width:118px">
      <p>Calibration is the foundation of accuracy. Our certified technicians perform rigorous, traceable calibration using test weights that meet or exceed industry standards. This service verifies your scale's performance and includes the necessary adjustments to bring it within compliance, particularly for Legal-for-Trade applications.</p>
      <p>We provide comprehensive documentation and certification reports crucial for audits, ensuring your business meets all regulatory requirements.</p>
    </div>
    <div class="photo" role="img" aria-label="Technicians in hard hats installing a weighbridge frame" style="left:144px;top:36px;width:124px;height:114px;border-radius:10px 0 0 0;background:linear-gradient(180deg,#c8d8e6,#a9a49a 50%,#7b8087)"></div>
    <div class="badge"><span>Harbor Lane Gauges</span></div>
  </section>

  <!-- 9 Preventative -->
  <section class="slide c1 r3">
    <div class="rule" style="left:16px;top:12px"></div>
    <div class="title" style="left:16px;top:24px">Preventative Service<br>and Maintenance</div>
    <div class="body" style="left:16px;top:55px;width:118px">
      <p>Protect your investment and minimise costly operational stoppages with our structured service plans. Our technicians conduct routine, detailed inspections, including cleaning, leveling, component checks (load cells, indicators), and minor adjustments.</p>
      <p>Regular preventative maintenance is key to identifying small issues before they escalate, extending the lifespan of your scales, and ensuring continuous, accurate performance in demanding industrial environments.</p>
    </div>
    <div class="photo" role="img" aria-label="Two workers in safety vests reviewing a tablet in a warehouse" style="left:142px;top:44px;width:122px;height:62px;border-radius:10px;background:linear-gradient(135deg,#6e6448,#c9b53a 50%,#4c5660)"></div>
    <div class="badge"><span>Harbor Lane Gauges</span></div>
  </section>

  <!-- 10 Repair -->
  <section class="slide c2 r3">
    <div class="rule" style="left:16px;top:12px"></div>
    <div class="title" style="left:16px;top:24px">Repair and<br>Emergency Service</div>
    <div class="photo" role="img" aria-label="Gloved hands repairing a scale circuit board" style="left:0;top:58px;width:155px;height:92px;background:linear-gradient(135deg,#e8ecef,#6e7e8c 55%,#1d3d5c)"></div>
    <div class="body" style="left:170px;top:58px;width:90px">
      <p>When a scale goes down, your business stops. We offer fast, reliable repair services for all makes and models of industrial and commercial scales. Our expert technicians are equipped to diagnose and fix a wide range of issues, from complex load cell failures and electronic component damage to physical wear and tear.</p>
      <p>We provide prompt on-site service to quickly restore full functionality, reducing your downtime and protecting your bottom line.</p>
    </div>
    <div class="badge"><span>Harbor Lane Gauges</span></div>
  </section>

  <!-- 11 Repair alt -->
  <section class="slide c3 r3">
    <div class="rule" style="left:16px;top:12px"></div>
    <div class="title" style="left:16px;top:24px">Repair and<br>Emergency Service</div>
    <div class="photo" role="img" aria-label="Gloved hands repairing a scale circuit board" style="left:0;top:58px;width:155px;height:92px;background:linear-gradient(135deg,#e8ecef,#6e7e8c 55%,#1d3d5c)"></div>
    <div class="body" style="left:170px;top:58px;width:90px">
      <p>When a scale goes down, your business stops. We offer fast, reliable repair services for all makes and models of industrial and commercial scales. Our expert technicians are equipped to diagnose and fix a wide range of issues, from complex load cell failures and electronic component damage to physical wear and tear.</p>
      <p>We provide prompt on-site service to quickly restore full functionality, reducing your downtime and protecting your bottom line.</p>
    </div>
    <div class="badge"><span>Harbor Lane Gauges</span></div>
  </section>

  <!-- 12 Our team -->
  <section class="slide c4 r3">
    <div class="photo" role="img" aria-label="Team of engineers in hard hats on a factory floor" style="left:118px;top:0;width:150px;height:28px;border-radius:0 0 0 8px;background:linear-gradient(90deg,#2c5f8a,#d8b23a 40%,#5d6a76)"></div>
    <div class="rule" style="left:16px;top:18px"></div>
    <div class="title" style="left:16px;top:25px">Our team</div>
    <div class="member" style="left:16px"><div class="ph">Photo</div><div class="bar dark">Name<small>Role</small></div><div class="txt">Short note on experience and focus area goes in this line.</div></div>
    <div class="member" style="left:77px"><div class="ph">Photo</div><div class="bar blue">Name<small>Role</small></div><div class="txt">Short note on experience and focus area goes in this line.</div></div>
    <div class="member" style="left:138px"><div class="ph">Photo</div><div class="bar dark">Name<small>Role</small></div><div class="txt">Short note on experience and focus area goes in this line.</div></div>
    <div class="member" style="left:199px"><div class="ph">Photo</div><div class="bar blue">Name<small>Role</small></div><div class="txt">Short note on experience and focus area goes in this line.</div></div>
    <div class="badge"><span>Harbor Lane Gauges</span></div>
  </section>

  <!-- 13 Team member -->
  <section class="slide c1 r4">
    <div class="abs" style="left:24px;top:24px;width:72px;height:72px;border-radius:50%;border:2px solid var(--red);display:flex;align-items:center;justify-content:center">
      <div style="width:62px;height:62px;border-radius:50%;background:var(--grey-soft);font-size:3.4px;color:#9a9a9a;display:flex;align-items:center;justify-content:center">Photo</div>
    </div>
    <div class="title" style="left:16px;top:112px;font-size:6.4px">Team Member Name</div>
    <div class="abs" style="left:16px;top:121px;font-size:3.6px;color:var(--grey)">Designation</div>
    <div class="item" style="top:26px"><div class="ic"></div><div><h4>Description heading</h4><p>Brief summary of this person's role and what they bring to the board and the wider business.</p></div></div>
    <div class="item" style="top:62px"><div class="ic"></div><div><h4>Qualification</h4><p>Degrees, certifications and technical training relevant to scales and measurement work.</p></div></div>
    <div class="item" style="top:98px"><div class="ic"></div><div><h4>Achievements</h4><p>Key milestones, projects delivered and results achieved for clients across the region.</p></div></div>
    <div class="badge"><span>Harbor Lane Gauges</span></div>
  </section>

  <!-- 14 Vision, Mission, Values -->
  <section class="slide c2 r4">
    <div class="rule" style="left:16px;top:12px"></div>
    <div class="title" style="left:16px;top:24px">Vision, Mission and Values</div>
    <div class="vcirc" style="left:76px;top:64px;background:var(--blue)"></div>
    <div class="vcirc" style="left:119px;top:86px;background:var(--charcoal)"></div>
    <div class="vcirc" style="left:162px;top:64px;background:var(--red)"></div>
    <div class="vlabel" style="left:16px;top:72px">Vision</div>
    <div class="vtext" style="left:16px;top:78px">To be the most trusted partner for accurate weighing in every industry we serve.</div>
    <div class="vlabel" style="left:127px;top:50px">Values</div>
    <div class="vtext" style="left:109px;top:56px;text-align:center">Accuracy, integrity and fast response.</div>
    <div class="vlabel" style="left:200px;top:72px">Mission</div>
    <div class="vtext" style="left:200px;top:78px">To keep our clients' scales precise, certified and always working.</div>
    <div class="badge"><span>Harbor Lane Gauges</span></div>
  </section>

  <!-- 15 Charts -->
  <section class="slide c3 r4">
    <div class="rule" style="left:16px;top:12px"></div>
    <div class="title" style="left:16px;top:24px">Charts and graphs style</div>
    <svg class="abs" style="left:14px;top:44px" width="165" height="100" viewBox="0 0 165 100" role="img" aria-label="Bar chart of three series across four categories">
      <text x="82" y="6" font-size="3.4" fill="#cf3a2c" text-anchor="middle" font-family="Poppins,sans-serif">Chart Title</text>
      <g stroke="#e6e6e6" stroke-width=".4">
        <line x1="14" y1="14" x2="160" y2="14"/><line x1="14" y1="28" x2="160" y2="28"/><line x1="14" y1="42" x2="160" y2="42"/><line x1="14" y1="56" x2="160" y2="56"/><line x1="14" y1="70" x2="160" y2="70"/>
      </g>
      <line x1="14" y1="84" x2="160" y2="84" stroke="#bfbfbf" stroke-width=".5"/>
      <g fill="#d9d9d9"><rect x="22" y="34" width="6" height="50"/><rect x="58" y="46" width="6" height="38"/><rect x="94" y="40" width="6" height="44"/><rect x="130" y="28" width="6" height="56"/></g>
      <g fill="#6b6f75"><rect x="29" y="58" width="6" height="26"/><rect x="65" y="36" width="6" height="48"/><rect x="101" y="58" width="6" height="26"/><rect x="137" y="52" width="6" height="32"/></g>
      <g fill="#2b5f8e"><rect x="36" y="62" width="6" height="22"/><rect x="72" y="62" width="6" height="22"/><rect x="108" y="50" width="6" height="34"/><rect x="144" y="18" width="6" height="66"/></g>
      <g font-size="2.8" fill="#6b6f75" text-anchor="middle" font-family="Poppins,sans-serif">
        <text x="32" y="90">Category 1</text><text x="68" y="90">Category 2</text><text x="104" y="90">Category 3</text><text x="140" y="90">Category 4</text>
        <text x="60" y="97">■ Series 1</text><text x="84" y="97">■ Series 2</text><text x="108" y="97">■ Series 3</text>
      </g>
      <g font-size="2.6" fill="#9a9a9a" text-anchor="end" font-family="Poppins,sans-serif">
        <text x="11" y="85">0</text><text x="11" y="71">1</text><text x="11" y="57">2</text><text x="11" y="43">3</text><text x="11" y="29">4</text><text x="11" y="15">5</text>
      </g>
    </svg>
    <div class="findings">
      <div class="tag">Key Findings</div>
      <p>Service contract revenue grew steadily across all four quarters of the year.</p>
      <p>Calibration demand peaked in the final quarter as audit deadlines approached.</p>
      <p>Truck scale sales remain the largest single driver of new business.</p>
    </div>
    <div class="badge"><span>Harbor Lane Gauges</span></div>
  </section>

  <!-- 16 Thank you -->
  <section class="slide c4 r4 thanks">
    <div class="photo" role="img" aria-label="Red truck parked at a loading dock" style="left:108px;top:40px;width:160px;height:110px;background:linear-gradient(180deg,rgba(255,255,255,0) 0%,#c7312a 30%,#a3261f 70%,#5e6469)"></div>
    <div class="brand" style="left:170px;top:8px;width:44px"><div class="dot"></div><div class="name" style="color:var(--charcoal)">HARBOR LANE GAUGES</div></div>
    <div class="title" style="left:16px;top:22px;font-size:13px;color:var(--white)">Thank you</div>
    <div class="title" style="left:16px;top:86px;font-size:6px;color:var(--white)">Contact us</div>
    <ul class="contact">
      <li><i></i>Address line 1<br>Address line 2<br>Address line 3</li>
      <li><i></i>000 000 0000</li>
      <li><i></i>Email address</li>
      <li><i></i>Website address</li>
    </ul>
  </section>

</main>
</body>
</html>
```